Need a business card design for a new business

The business is going to be called "The Maple Lectern" - it is an online training company that provides Instructor Lead training to students at any destination in the world
The reference to cloud is the internet and classroom reference will be a computer at the students and instructors end

We will need a Web site and stationary and advertising material developed over time but for now require the business cards only

So if we are happy with the business card then we will use the same designers for the other requirments of the business as it evolves

Industry/Entity Type

Advertising

```html
<!DOCTYPE html>
<html lang="en">
<head>
<meta charset="utf-8">
<title>The Maple Lectern — Business Cards</title>
<link rel="stylesheet" href="https://fonts.googleapis.com/css2?family=Jost:wght@500;600;700&display=swap">
<style>
  :root {
    --backdrop: #5a5a5a;
    --card-light: #52bfe8;
    --card-mid: #41afdf;
    --card-deep: #309fd2;
    --sheen: rgba(255,255,255,0.10);
    --ink-white: #ffffff;
    --ink-band: #1b6f90;
    --band: #ffffff;
  }
  * { box-sizing: border-box; margin: 0; padding: 0; }
  html, body {
    width: 1200px; height: 1200px; overflow: hidden;
    background: var(--backdrop);
    font-family: "Jost", "Futura", sans-serif;
  }
  .card {
    position: absolute;
    width: 746px; height: 457px;
    overflow: hidden;
    background:
      linear-gradient(148deg, transparent 0 58%, var(--sheen) 58% 100%),
      linear-gradient(160deg, var(--card-light) 0%, var(--card-mid) 45%, var(--card-deep) 100%);
  }
  .card--front { left: 90px; top: 105px; }
  .card--back  { left: 363px; top: 660px; width: 747px; }

  .wordmark {
    position: absolute;
    color: var(--ink-white);
    font-weight: 700;
    text-transform: uppercase;
    text-align: right;
    line-height: 1;
    letter-spacing: 0.01em;
  }
  .card--front .wordmark { right: 28px; top: 92px; }
  .card--front .wordmark__top { font-size: 84px; display: block; }
  .card--front .wordmark__bottom { font-size: 92px; display: block; margin-top: 30px; }

  .url-band {
    position: absolute; left: 0; right: 0; top: 383px; height: 49px;
    background: var(--band);
    color: var(--ink-band);
    font-weight: 700; font-size: 42px; line-height: 49px;
    text-align: center;
  }

  .card--back .wordmark { right: 24px; top: 50px; }
  .card--back .wordmark__top { font-size: 42px; display: block; }
  .card--back .wordmark__bottom { font-size: 44px; display: block; margin-top: 14px; }

  .role {
    position: absolute; left: 60px; top: 80px;
    color: var(--ink-white); font-weight: 600; font-size: 42px; line-height: 1.2;
  }
  .address {
    position: absolute; right: 92px; top: 194px;
    color: var(--ink-white); font-weight: 600; font-size: 34px;
  }
  .contact {
    position: absolute; right: 22px; top: 305px;
    list-style: none;
  }
  .contact__item {
    display: flex; align-items: center; justify-content: flex-end;
    height: 47px;
    color: var(--ink-white); font-weight: 600; font-size: 34px;
    letter-spacing: 0.02em;
  }
  .contact__icon { width: 44px; height: 36px; margin-left: 28px; flex: none; }
</style>
</head>
<body>

<section class="card card--front" aria-label="Card front">
  <h1 class="wordmark">
    <span class="wordmark__top">The Maple</span>
    <span class="wordmark__bottom">Lectern</span>
  </h1>
  <div class="url-band">www.themaplelectern.com</div>
</section>

<section class="card card--back" aria-label="Card back">
  <p class="role">Project Owner</p>
  <h2 class="wordmark">
    <span class="wordmark__top">The Maple</span>
    <span class="wordmark__bottom">Lectern</span>
  </h2>
  <p class="address">Adress in here</p>
  <ul class="contact">
    <li class="contact__item">01&nbsp; 234&nbsp; 567890
      <svg class="contact__icon" viewBox="0 0 44 36" aria-hidden="true">
        <rect x="13" y="2" width="3" height="8" fill="#fff"/>
        <rect x="12" y="8" width="20" height="27" rx="3" fill="#fff"/>
        <rect x="16" y="12" width="12" height="8" fill="#41afdf"/>
      </svg>
    </li>
    <li class="contact__item">www.themaplelectern.com
      <svg class="contact__icon" viewBox="0 0 44 36" aria-hidden="true">
        <path d="M14 4 L14 28 L20 22 L25 33 L29 31 L24 21 L32 21 Z" fill="#fff"/>
      </svg>
    </li>
    <li class="contact__item">hello@themaplelectern.com
      <svg class="contact__icon" viewBox="0 0 44 36" aria-hidden="true">
        <rect x="4" y="6" width="38" height="26" rx="2" fill="#fff"/>
        <path d="M4 8 L23 21 L42 8" fill="none" stroke="#41afdf" stroke-width="3"/>
      </svg>
    </li>
  </ul>
</section>

</body>
</html>
```